Business card design Needed for new logo / Construction business, home extensions and new builds

We need a business card design using our new logo files which i will attach to this project :)

We are a small construction business specialising in home extensions, new builds and property development. We are very ambitious and would appreciate professional and elegant designs for our new business card.

Very serious about using the services on BriefNest and recently acquired our new logo from here :)

Please get involved, i will feedback when i can as i am very busy but can respond daily, thanks

Target Market(s)

People that want to build onto their houses, new building developments or adding too their existing property

Industry/Entity Type

Construction

Contact Information for Business Card

Hollin Marsh Construction, Tobias Renwick (Managing Director), Tel 07822200444, email - info@hollin-marsh, www.hollin-marsh.co.uk

Colors

Designer to choose colors to be used in the design.

Requirements
Must have
• I like a deep grey on the back please. A lot of you have provided black from and back, try mixing things up a little. The black looks cool 😎 Thanks

```html
<!DOCTYPE html>
<html lang="en">
<head>
<meta charset="utf-8">
<title>Hollin Marsh Construction – Business Card</title>
<link rel="stylesheet" href="https://fonts.googleapis.com/css2?family=Montserrat:wght@400;500;700&display=swap">
<style>
  :root {
    --stage: #4a4a4a;
    --card-front: #141414;
    --card-back: #2a2a2b;
    --gold: #d9a630;
    --text-light: #f2f2f2;
  }
  * { box-sizing: border-box; margin: 0; padding: 0; }
  html, body {
    width: 1200px; height: 689px; overflow: hidden;
    background: var(--stage);
    font-family: "Montserrat", sans-serif;
  }
  .canvas {
    position: relative; width: 1200px; height: 689px;
    display: flex; align-items: center; justify-content: center; gap: 40px;
  }
  .card {
    position: relative; width: 540px; height: 309px;
    border-radius: 18px; overflow: hidden;
    box-shadow: 0 12px 30px rgba(0, 0, 0, 0.35);
  }
  .card--front { background: var(--card-front); }
  .card--back  { background: var(--card-back); }

  .brand {
    position: absolute; display: flex; align-items: center; gap: 10px;
    color: var(--gold); font-weight: 700; text-transform: uppercase;
    letter-spacing: 0.08em; white-space: nowrap;
  }
  .brand__square { width: 13px; height: 13px; background: var(--gold); flex: none; }
  .card--front .brand {
    left: 50%; top: 50%; transform: translate(-50%, -50%); font-size: 23px;
  }
  .card--back .brand {
    left: 320px; top: 70px; transform: translateX(-50%); font-size: 18px;
  }
  .card--back .brand .brand__square { width: 10px; height: 10px; }

  .person {
    position: absolute; right: 240px; top: 160px; text-align: right;
    color: var(--text-light); font-size: 13px; line-height: 1.5;
  }
  .person__name {
    color: var(--gold); font-weight: 700; font-size: 20px;
    text-transform: uppercase; letter-spacing: 0.02em; margin-bottom: 2px;
  }
  .divider {
    position: absolute; left: 318px; top: 152px; width: 1.5px; height: 104px;
    background: var(--gold);
  }
  .contacts {
    position: absolute; left: 338px; top: 160px; list-style: none;
    color: var(--text-light); font-size: 13px;
  }
  .contacts li { display: flex; align-items: center; gap: 10px; height: 24px; }
  .contacts svg { width: 14px; height: 14px; flex: none; }
  .edge-line {
    position: absolute; left: 0; right: 0; bottom: 0; height: 2px;
    background: var(--gold);
  }
</style>
</head>
<body>
<main class="canvas">
  <section class="card card--front" aria-label="Business card front">
    <div class="brand"><span class="brand__square"></span>Hollin Marsh Construction</div>
  </section>

  <section class="card card--back" aria-label="Business card back">
    <div class="brand"><span class="brand__square"></span>Hollin Marsh Construction</div>

    <div class="person">
      <p class="person__name">Tobias Renwick</p>
      <p>Managing Director</p>
      <p>Your address, City</p>
      <p>State, Zip 1234</p>
    </div>

    <div class="divider"></div>

    <ul class="contacts">
      <li>
        <svg viewBox="0 0 16 16" aria-hidden="true"><path fill="var(--gold)" d="M3.6 1.5l2.2 2.6-1.3 1.7c.9 2 2.4 3.5 4.4 4.4l1.7-1.3 2.6 2.2-1.2 2.3C6.6 15.1.9 9.4 1.3 2.7z"/></svg>
        07822200444
      </li>
      <li>
        <svg viewBox="0 0 16 16" aria-hidden="true"><rect x="1" y="3" width="14" height="10" rx="1" fill="var(--gold)"/><path d="M1.5 3.8L8 9l6.5-5.2" stroke="var(--card-back)" stroke-width="1.3" fill="none"/></svg>
        info@hollin-marsh
      </li>
      <li>
        <svg viewBox="0 0 16 16" aria-hidden="true"><circle cx="8" cy="8" r="7" fill="var(--gold)"/><path d="M1 8h14M8 1c-3 3.5-3 10.5 0 14M8 1c3 3.5 3 10.5 0 14" stroke="var(--card-back)" stroke-width="1" fill="none"/></svg>
        www.hollin-marsh.co.uk
      </li>
    </ul>

    <div class="edge-line"></div>
  </section>
</main>
</body>
</html>
```